Business Card Design

www.bellwaterridge.com.au

Bellwater Ridge Bed and Breakfast
A unique property with spectacular views situated in a peaceful quiet court surrounded by other quality homes. Set back from the street, this wonderful residence has plenty of space. The huge paved driveway has tonnes of off street parking

Relax in the beautifully landscaped lawn area with mature trees. The stunning balcony & deck is an ideal place to sit & watch the spectacular sunsets through the tree tops. Just wonderful!

The self-contained Bed and Breakfast has its own separate entrance door and consists of a large lounge/ kitchenette with sink & a separate bedroom. The bathroom has a glass shower screen, toilet & vanity unit.
If you are looking for your own piece of paradise in an ideal established setting with plenty of room then you must stay at Bellwater ridge
This really is a slice of Heaven so come & stay!

- Established landscaped gardens & lawn areas
- paved driveway - loads of off street parking
- Splendid balcony with glorious views
- Close to shopping & transport

We welcome you to relax and unwind in the charm of our modern country feel bed and breakfast in the Northern Suburbs of Adelaide, offering privacy and relaxation, it is perfect for couples
This self-contained bed & breakfast will provide you with a “home away from home”, including breakfast provisions and all the comfort and modern conveniences you’d expect Bellwater Ridge is perfect whether you’re on a holiday visit to Adelaide or here for business.
Enjoy the many activities Adelaide has to offer, we are positioned in the Northern Suburbs for you to easily travel to the Adelaide Hills or Barossa Wine region.
Bellwater Ridge B & B is in a fantastic location for whatever you want to do on your visit to South Australia. Nestled within walking distance to the Cobbler Creek or visit our world renowned wine regions. Of course, we can help and point you in the right direction.

Shopping

14 Bellwater Court
Tarrowin Heights WR 7342

Dennis & Maureen Pellham
0412 555 648 or 0413 555 927
www.bellwaterridge.com.au
dennis@bellwaterridge.com.au

```html
<!DOCTYPE html>
<html lang="en">
<head>
<meta charset="utf-8">
<title>Bellwater Ridge Bed and Breakfast – Business Card</title>
<link rel="stylesheet" href="https://fonts.googleapis.com/css2?family=Rye&family=Alfa+Slab+One&display=swap">
<style>
  :root {
    --page: #ffffff;
    --ink: #0d0b0a;
    --ink-soft: #2a2622;
    --glow: #ffffff;
  }
  html, body {
    margin: 0;
    padding: 0;
    width: 1200px;
    height: 693px;
    overflow: hidden;
    background: var(--page);
  }
  .business-card {
    display: block;
    width: 1200px;
    height: 693px;
  }
  .card-title {
    font-family: "Rye", serif;
    fill: var(--ink);
  }
  .card-address {
    font-family: "Rye", serif;
    fill: var(--ink);
  }
  .card-contact {
    font-family: "Alfa Slab One", serif;
    fill: var(--ink-soft);
  }
</style>
</head>
<body>
<svg class="business-card" viewBox="0 0 1200 693" xmlns="http://www.w3.org/2000/svg">
  <defs>
    <linearGradient id="landscape-tones" x1="0" y1="0" x2="0" y2="1">
      <stop offset="0" stop-color="#5e3d1c"/>
      <stop offset="0.07" stop-color="#e9a540"/>
      <stop offset="0.22" stop-color="#dc8a2c"/>
      <stop offset="0.33" stop-color="#b8743c"/>
      <stop offset="0.42" stop-color="#8a6f9a"/>
      <stop offset="0.52" stop-color="#4a5aa0"/>
      <stop offset="0.64" stop-color="#34417c"/>
      <stop offset="0.72" stop-color="#3a3f4a"/>
      <stop offset="0.8" stop-color="#4d6838"/>
      <stop offset="1" stop-color="#2a3a1c"/>
    </linearGradient>
    <radialGradient id="sun-glow" cx="0.38" cy="0.03" r="0.35">
      <stop offset="0" stop-color="#fff6d8" stop-opacity="0.95"/>
      <stop offset="0.3" stop-color="#f7c35a" stop-opacity="0.6"/>
      <stop offset="1" stop-color="#f0a030" stop-opacity="0"/>
    </radialGradient>
    <filter id="soft-edge" x="-5%" y="-5%" width="110%" height="110%">
      <feGaussianBlur stdDeviation="3"/>
    </filter>
    <filter id="white-halo" x="-10%" y="-40%" width="120%" height="180%">
      <feMorphology in="SourceAlpha" operator="dilate" radius="3" result="grown"/>
      <feGaussianBlur in="grown" stdDeviation="6" result="blur"/>
      <feFlood flood-color="#ffffff" flood-opacity="0.9"/>
      <feComposite in2="blur" operator="in" result="halo"/>
      <feMerge>
        <feMergeNode in="halo"/>
        <feMergeNode in="SourceGraphic"/>
      </feMerge>
    </filter>
  </defs>

  <g role="img" aria-label="Photograph of a sunset sky over snow-capped mountains with an old timber barn and fenced green pasture">
    <rect x="48" y="48" width="1118" height="609" fill="url(#landscape-tones)" filter="url(#soft-edge)"/>
    <rect x="48" y="48" width="1118" height="609" fill="url(#sun-glow)"/>
  </g>

  <g class="card-heading" filter="url(#white-halo)">
    <text class="card-title" x="243" y="260" font-size="50" textLength="694" lengthAdjust="spacingAndGlyphs">BELLWATER RIDGE</text>
    <text class="card-title" x="120" y="318" font-size="52" textLength="989" lengthAdjust="spacingAndGlyphs">BED AND BREAKFAST</text>
  </g>

  <g class="card-location" filter="url(#white-halo)">
    <text class="card-address" x="331" y="375" font-size="30" textLength="532" lengthAdjust="spacingAndGlyphs">14 BELLWATER COURT</text>
    <text class="card-address" x="189" y="411" font-size="30" textLength="868" lengthAdjust="spacingAndGlyphs">TARROWIN HEIGHTS WR 7342</text>
  </g>

  <g class="card-details" filter="url(#white-halo)">
    <text class="card-contact" x="78" y="528" font-size="38" textLength="750" lengthAdjust="spacingAndGlyphs">PHONE: 0412 555 648 OR 0413 555 927</text>
    <text class="card-contact" x="78" y="571" font-size="38" textLength="680" lengthAdjust="spacingAndGlyphs">WWW.BELLWATERRIDGE.COM.AU</text>
    <text class="card-contact" x="78" y="626" font-size="38" textLength="740" lengthAdjust="spacingAndGlyphs">DENNIS@BELLWATERRIDGE.COM.AU</text>
  </g>
</svg>
</body>
</html>
```